First of a series of workplace posters- our values statement

To produce a high quality poster of our values, we would like one in a3 and one in a4 both full colour
By utilising the supplied text , the intent is to produce a really striking poster for all our work places, which set out our company values. we are looking for really strong graphical elements which support the message visually . This will be the first of a series of posters, so we are looking to establish at stylistic theme for all with this one. for more on our business,

Target Market(s)

Internal and external audiences, our clients are all tier one companies

Requirements
Must have
• contemporary design rather than conservative, visually striking
• Must be clearly readable from a reasonable distance
Nice to have
• would be nice to tie in to the blue and greens of our logo in similar fashion to our website. www.qrtbuildwise.com
Should not have
• Difficult to read fonts,

```html
<!DOCTYPE html>
<html lang="en">
<head>
<meta charset="utf-8">
<title>QRT Buildwise – Our Values Poster</title>
<link href="https://fonts.googleapis.com/css2?family=Fredoka:wght@300;500;600&family=League+Spartan:wght@800&display=swap" rel="stylesheet">
<style>
  :root {
    --navy: #05306f;
    --green: #68b332;
    --headline-green: #6cb52d;
    --white: #ffffff;
    --black: #050505;
    --grass-light: #4f9a32;
    --grass-dark: #1d5816;
    --sky: #e4e8ea;
  }
  * { box-sizing: border-box; margin: 0; padding: 0; }
  html, body { width: 927px; height: 1200px; overflow: hidden; background: var(--white); }
  .poster {
    position: relative; width: 927px; height: 1200px; overflow: hidden;
    background: var(--white);
    font-family: "Fredoka", sans-serif;
  }
  .field-photo {
    position: absolute; left: 0; top: 560px; width: 927px; height: 640px;
    background: linear-gradient(180deg,
      rgba(255,255,255,0) 0%,
      var(--sky) 14%,
      #c9d3cf 20%,
      var(--grass-light) 22%,
      #3f8a2a 45%,
      var(--grass-dark) 100%);
  }
  .shapes { position: absolute; inset: 0; }
  .brand {
    position: absolute; left: 712px; top: 48px;
    display: flex; align-items: center; gap: 8px;
  }
  .brand-dot { width: 24px; height: 24px; border-radius: 50%; background: var(--green); }
  .brand-name { font-family: "Fredoka", sans-serif; font-weight: 600; font-size: 25px; color: var(--navy); }

  .headline {
    position: absolute; left: 59px; top: 92px;
    font-family: "League Spartan", sans-serif; font-weight: 800;
    color: var(--headline-green); letter-spacing: -1px; line-height: 1;
  }
  .headline .line-1 { display: block; font-size: 56px; }
  .headline .line-2 { display: block; font-size: 46px; margin-top: 3px; }
  .smile {
    position: absolute; left: 584px; top: 143px;
    font-family: "League Spartan", sans-serif; font-weight: 800;
    font-size: 38px; color: var(--white);
  }
  .intro {
    position: absolute; left: 109px; top: 205px;
    font-weight: 300; font-size: 23px; color: var(--white); letter-spacing: -0.5px;
  }
  .values-list { list-style: none; position: absolute; left: 59px; top: 0; }
  .values-list li {
    position: absolute; left: 0; width: 560px;
    display: flex; align-items: center; gap: 20px;
    font-weight: 600; font-size: 21.5px; line-height: 26px;
    color: var(--white); letter-spacing: -0.4px;
  }
  .bullet { flex: none; width: 17px; height: 17px; }

  .safety-title {
    position: absolute; right: 66px; top: 697px; text-align: right;
    font-family: "League Spartan", sans-serif; font-weight: 800; letter-spacing: -1px; line-height: 1;
  }
  .safety-title .kicker { display: block; font-size: 27px; color: var(--navy); }
  .safety-title .main { display: block; font-size: 42px; color: var(--white); margin-top: 4px; }
  .safety-statement {
    position: absolute; left: 140px; top: 782px; width: 726px;
    font-weight: 300; font-size: 12.6px; line-height: 14.5px;
    color: var(--navy); letter-spacing: -0.2px;
  }
  .safety-list { list-style: none; position: absolute; right: 0; top: 0; }
  .safety-list li {
    position: absolute; right: 74px; width: 640px;
    display: flex; justify-content: flex-end; align-items: center; gap: 18px;
    text-align: right;
    font-weight: 600; font-size: 20.5px; line-height: 22px;
    color: var(--white); letter-spacing: -0.4px; white-space: nowrap;
  }
</style>
</head>
<body>
<main class="poster">
  <div class="field-photo" role="img" aria-label="Photograph of a green grass field under a misty sky"></div>

  <svg class="shapes" width="927" height="1200" viewBox="0 0 927 1200" aria-hidden="true">
    <circle cx="299" cy="353" r="404" fill="var(--navy)"/>
    <circle cx="696" cy="478" r="71" fill="var(--black)"/>
    <circle cx="717" cy="478" r="91" fill="var(--green)"/>
    <ellipse cx="743" cy="479" rx="73" ry="83" fill="none" stroke="var(--navy)" stroke-width="2.5"/>
    <circle cx="755" cy="299" r="8" fill="var(--green)"/>
    <circle cx="769" cy="296" r="13" fill="none" stroke="var(--navy)" stroke-width="2.5"/>
    <circle cx="757" cy="351" r="20" fill="var(--green)"/>
    <circle cx="757" cy="351" r="26" fill="none" stroke="var(--navy)" stroke-width="2.5"/>
    <path d="M46 183 Q120 178 199 180" stroke="var(--white)" stroke-width="4" stroke-linecap="round" fill="none"/>
    <path d="M427 772 Q490 768 550 770" stroke="var(--green)" stroke-width="4" stroke-linecap="round" fill="none"/>
    <circle cx="90" cy="1107" r="258" fill="rgba(8,38,10,0.55)"/>
    <circle cx="21" cy="1101" r="266" fill="none" stroke="var(--white)" stroke-width="2"/>
    <ellipse cx="60" cy="772" rx="23" ry="32" fill="rgba(8,38,10,0.6)" stroke="var(--white)" stroke-width="2.5"/>
  </svg>

  <div class="brand">
    <span class="brand-dot"></span>
    <span class="brand-name">QRT Buildwise</span>
  </div>

  <h1 class="headline">
    <span class="line-1">WE VALUE OUR PEOPLE</span>
    <span class="line-2">ABOVE EVERYTHING ELSE</span>
  </h1>
  <span class="smile">:)</span>

  <p class="intro">We demonstrate this by:</p>

  <ul class="values-list">
    <li style="top:258px"><svg class="bullet" viewBox="0 0 20 20"><circle cx="10" cy="10" r="9" fill="var(--green)"/><circle cx="11" cy="9" r="4" fill="none" stroke="var(--navy)" stroke-width="2"/></svg><span>Providing safe, positive, enjoyable workplaces where everyone feels valued and respected.</span></li>
    <li style="top:340px"><svg class="bullet" viewBox="0 0 20 20"><circle cx="10" cy="10" r="9" fill="var(--green)"/><circle cx="11" cy="9" r="4" fill="none" stroke="var(--navy)" stroke-width="2"/></svg><span>Providing careers, not jobs, we grow together.</span></li>
    <li style="top:392px"><svg class="bullet" viewBox="0 0 20 20"><circle cx="10" cy="10" r="9" fill="var(--green)"/><circle cx="11" cy="9" r="4" fill="none" stroke="var(--navy)" stroke-width="2"/></svg><span>Encouraging inclusion, participation<br>and collaboration.</span></li>
    <li style="top:468px"><svg class="bullet" viewBox="0 0 20 20"><circle cx="10" cy="10" r="9" fill="var(--green)"/><circle cx="11" cy="9" r="4" fill="none" stroke="var(--navy)" stroke-width="2"/></svg><span>Recognising and rewarding contribution<br>and excellence.</span></li>
    <li style="top:553px"><svg class="bullet" viewBox="0 0 20 20"><circle cx="10" cy="10" r="9" fill="var(--green)"/><circle cx="11" cy="9" r="4" fill="none" stroke="var(--navy)" stroke-width="2"/></svg><span>Supporting our people through tough times.</span></li>
    <li style="top:604px"><svg class="bullet" viewBox="0 0 20 20"><circle cx="10" cy="10" r="9" fill="var(--green)"/><circle cx="11" cy="9" r="4" fill="none" stroke="var(--navy)" stroke-width="2"/></svg><span>Fostering healthy work life balance.</span></li>
  </ul>

  <h2 class="safety-title">
    <span class="kicker">ALL OUR WORKPLACES</span>
    <span class="main">ARE SAFE WORK PLACES</span>
  </h2>

  <p class="safety-statement">There is nothing more important to us than our team members going home healthy and safe every day, we wont accept anything less. We believe workplace safety is a management choice, by providing safe work systems and education we achieve our daily goal of Zero Harm.</p>

  <ul class="safety-list">
    <li style="top:854px"><span>Take the time to make our work areas safe<br>, whatever it takes.</span><svg class="bullet" viewBox="0 0 20 20"><circle cx="10" cy="10" r="9" fill="none" stroke="var(--navy)" stroke-width="2.5"/><circle cx="11" cy="10" r="4" fill="var(--navy)"/></svg></li>
    <li style="top:918px"><span>Don't accept shortcuts.</span><svg class="bullet" viewBox="0 0 20 20"><circle cx="10" cy="10" r="9" fill="none" stroke="var(--navy)" stroke-width="2.5"/><circle cx="11" cy="10" r="4" fill="var(--navy)"/></svg></li>
    <li style="top:961px"><span>Look out for each other.</span><svg class="bullet" viewBox="0 0 20 20"><circle cx="10" cy="10" r="9" fill="none" stroke="var(--navy)" stroke-width="2.5"/><circle cx="11" cy="10" r="4" fill="var(--navy)"/></svg></li>
    <li style="top:1003px"><span>Investigate our incidents and learn from them, no repeats.</span><svg class="bullet" viewBox="0 0 20 20"><circle cx="10" cy="10" r="9" fill="none" stroke="var(--navy)" stroke-width="2.5"/><circle cx="11" cy="10" r="4" fill="var(--navy)"/></svg></li>
    <li style="top:1046px"><span>Are constantly looking for ways to improve the safety of<br>our workplaces and the health of our team members.</span><svg class="bullet" viewBox="0 0 20 20"><circle cx="10" cy="10" r="9" fill="none" stroke="var(--navy)" stroke-width="2.5"/><circle cx="11" cy="10" r="4" fill="var(--navy)"/></svg></li>
    <li style="top:1110px"><span>Think safe, work safe, go home safe!</span><svg class="bullet" viewBox="0 0 20 20"><circle cx="10" cy="10" r="9" fill="none" stroke="var(--navy)" stroke-width="2.5"/><circle cx="11" cy="10" r="4" fill="var(--navy)"/></svg></li>
  </ul>
</main>
</body>
</html>
```